Zielgruppe
Scharf schiessen für Jedermann
Aufgabenstellung
Wir möchten unser Produkt auf einer A4 Seite in einem Eroitk Magazin präsentieren.
Es soll den Lesern Lust machen zu uns zu kommen und mit scharfen Waffen zu schiessen.
kernpunkte :
1. Berlin
2. Waffen
3. Event
4. Entertainment
Es daff keinen XXX Bezug haben.
Bilder Content darf von unser Webseite: www.zielwerk-beispiel.net genutzt werden.

```html
<!DOCTYPE html>
<html lang="de">
<head>
<meta charset="utf-8">
<title>Zielwerk – Schießen für Jedermann</title>
<link href="https://fonts.googleapis.com/css2?family=Ubuntu:ital,wght@0,500;0,700;1,500;1,700&display=swap" rel="stylesheet">
<style>
  :root {
    --brand-blue: #1e69a4;
    --band-stripe: #2472b0;
    --navy: #1f2c47;
    --tag-text: #27344f;
    --paper: #f4f5f7;
    --skyline: #1c3258;
    --lower-bg: #5d86b5;
    --lower-bg-dark: #3f6592;
    --white: #ffffff;
  }
  * { margin: 0; padding: 0; box-sizing: border-box; }
  html, body { width: 873px; height: 1200px; overflow: hidden; background: #e9ebee; }
  .page {
    position: relative; width: 873px; height: 1200px; overflow: hidden;
    font-family: "Ubuntu", sans-serif; color: var(--white);
  }
  .page > svg.art { position: absolute; inset: 0; }
  .brand {
    position: absolute; left: 62px; top: 448px;
    display: flex; align-items: center; gap: 12px;
  }
  .brand-dot { width: 20px; height: 20px; border-radius: 50%; background: var(--white); }
  .brand-name { font-size: 50px; font-weight: 700; color: var(--white); letter-spacing: 1px; line-height: 1; }
  .brand-slogan {
    position: absolute; left: 96px; top: 503px;
    font-size: 11px; font-style: italic; font-weight: 500; color: #cfe0f0;
  }
  .tag {
    position: absolute; display: flex; align-items: center; gap: 12px;
    font-size: 41px; line-height: 1; font-weight: 700; font-style: italic; color: var(--tag-text);
  }
  .tag svg { flex: none; }
  .tag-spass { left: 600px; top: 252px; }
  .tag-events { left: 552px; top: 353px; }
  .tag-erlebnis { left: 508px; top: 454px; }
  .contact { position: absolute; left: 524px; top: 560px; font-style: italic; font-weight: 700; }
  .contact-lead { font-size: 21px; line-height: 28px; margin-bottom: 4px; }
  .contact-row { display: flex; align-items: center; gap: 34px; font-size: 21px; line-height: 30px; }
  .contact-row svg { flex: none; }
  .headline {
    position: absolute; left: 56px; top: 740px;
    font-size: 64px; line-height: 70px; font-weight: 700; font-style: italic;
    text-shadow: 2px 3px 4px rgba(0,0,0,.45);
  }
  .body-copy {
    position: absolute; left: 53px; top: 928px; width: 574px;
    column-count: 2; column-gap: 18px;
    font-size: 12.4px; line-height: 19.2px; font-weight: 700;
    text-align: justify; hyphens: auto;
  }
</style>
</head>
<body>
<div class="page">
  <svg class="art" width="873" height="1200" viewBox="0 0 873 1200">
    <defs>
      <linearGradient id="range-left" x1="0" y1="0" x2="1" y2="1">
        <stop offset="0" stop-color="#6f6a62"/><stop offset="1" stop-color="#3d3a37"/>
      </linearGradient>
      <linearGradient id="range-mid" x1="0" y1="0" x2="0" y2="1">
        <stop offset="0" stop-color="#7a6a45"/><stop offset=".5" stop-color="#8d8f95"/><stop offset="1" stop-color="#5a4e3f"/>
      </linearGradient>
      <linearGradient id="range-right" x1="0" y1="0" x2="0" y2="1">
        <stop offset="0" stop-color="#6b6c70"/><stop offset="1" stop-color="#a89a84"/>
      </linearGradient>
      <linearGradient id="lower-photo" x1="0" y1="0" x2="0" y2="1">
        <stop offset="0" stop-color="#5d86b5"/><stop offset="1" stop-color="#3f6592"/>
      </linearGradient>
      <linearGradient id="skyline-fade" x1="0" y1="0" x2="0" y2="1">
        <stop offset="0" stop-color="#1e69a4"/><stop offset="1" stop-color="#1c3258"/>
      </linearGradient>
    </defs>

    <!-- lower photo background -->
    <rect role="img" aria-label="Foto: unscharfer Blick in eine Schießbahn, blau eingefärbt" x="0" y="718" width="873" height="482" fill="url(#lower-photo)"/>

    <!-- photo strip -->
    <polygon role="img" aria-label="Foto: Schützin mit Gehörschutz feuert eine Pistole am Schießstand ab" points="0,0 378,0 195,409 0,409" fill="url(#range-left)"/>
    <polygon role="img" aria-label="Foto: Schütze im grauen Pullover zielt mit einem Gewehr" points="378,0 676,0 496,409 195,409" fill="url(#range-mid)"/>
    <polygon role="img" aria-label="Foto: Trainer erklärt einer Schützin die Waffenhaltung" points="676,0 873,0 873,409 496,409" fill="url(#range-right)"/>
    <line x1="378" y1="0" x2="195" y2="409" stroke="#fff" stroke-width="3"/>
    <line x1="676" y1="0" x2="496" y2="409" stroke="#fff" stroke-width="3"/>

    <!-- crosshairs -->
    <g fill="none" stroke="#fff" stroke-width="2">
      <circle cx="229" cy="184" r="38"/><circle cx="229" cy="184" r="10"/>
      <path d="M229 142v84M187 184h84"/>
      <circle cx="541" cy="155" r="79"/><circle cx="541" cy="155" r="22"/>
      <path d="M541 69v172M455 155h172"/>
      <circle cx="737" cy="77" r="38"/><circle cx="737" cy="77" r="10"/>
      <path d="M737 35v84M695 77h84"/>
    </g>

    <!-- blue band -->
    <rect x="0" y="409" width="873" height="309" fill="var(--brand-blue)"/>
    <rect x="0" y="409" width="873" height="14" fill="var(--band-stripe)"/>

    <!-- tag bars -->
    <rect x="621" y="233" width="252" height="81" fill="var(--paper)"/>
    <rect x="575" y="335" width="298" height="80" fill="var(--paper)"/>
    <polygon points="550,436 873,436 873,515 524,515" fill="var(--paper)"/>

    <!-- skyline area -->
    <rect role="img" aria-label="Illustration: Silhouette der Berliner Skyline" x="0" y="611" width="485" height="107" fill="url(#skyline-fade)"/>

    <!-- headline band -->
    <polygon points="0,717 470,717 440,786 668,786 625,902 0,902" fill="var(--navy)" opacity=".93"/>
  </svg>

  <div class="brand"><span class="brand-dot"></span><span class="brand-name">ZIELWERK</span></div>
  <div class="brand-slogan">Schießen für jedermann!</div>

  <div class="tag tag-spass">
    <svg width="44" height="44" viewBox="0 0 44 44" fill="none" stroke="#27344f" stroke-width="3"><circle cx="22" cy="22" r="19"/><circle cx="22" cy="22" r="7"/><path d="M22 0v44M0 22h44"/></svg>SPASS
  </div>
  <div class="tag tag-events">
    <svg width="44" height="44" viewBox="0 0 44 44" fill="none" stroke="#27344f" stroke-width="3"><circle cx="22" cy="22" r="19"/><circle cx="22" cy="22" r="7"/><path d="M22 0v44M0 22h44"/></svg>EVENTS
  </div>
  <div class="tag tag-erlebnis">
    <svg width="44" height="44" viewBox="0 0 44 44" fill="none" stroke="#27344f" stroke-width="3"><circle cx="22" cy="22" r="19"/><circle cx="22" cy="22" r="7"/><path d="M22 0v44M0 22h44"/></svg>ERLEBNIS
  </div>

  <div class="contact">
    <p class="contact-lead">Lassen Sie sich beraten:</p>
    <p class="contact-row">
      <svg width="20" height="15" viewBox="0 0 20 15"><rect width="20" height="15" rx="2" fill="#fff"/><path d="M1 2l9 7 9-7" fill="none" stroke="#1e69a4" stroke-width="2"/></svg>
      info@zielwerk-beispiel.net
    </p>
    <p class="contact-row">
      <svg width="20" height="18" viewBox="0 0 24 24"><path fill="#fff" d="M6.6 10.8a15 15 0 006.6 6.6l2.2-2.2a1 1 0 011-.25 11.4 11.4 0 003.6.57 1 1 0 011 1V20a1 1 0 01-1 1A17 17 0 013 4a1 1 0 011-1h3.5a1 1 0 011 1c0 1.25.2 2.45.57 3.57a1 1 0 01-.25 1z"/></svg>
      030 555 012 345
    </p>
  </div>

  <h1 class="headline">SCHIESSEN<br>FÜR JEDERMANN</h1>

  <div class="body-copy">
    <p>Die meisten Menschen kennen Handfeuerwaffen nur aus den großen Hollywood-Filmen auf der Kinoleinwand, dabei ist der Schießsport schon seit Jahrhunderten eine etablierte Sportart und gar nicht so unzugänglich, wie viele sicherlich glauben: Sie benötigen weder einen Waffenschein noch besondere Dokumente oder Zeugnisse, um bei Zielwerk eine Waffe in die Hand zu nehmen und abfeuern zu dürfen. Schauen Sie nicht weiter Actionfilme und träumen nur davon, eine dieser Waffen selbst in die Hand zu nehmen und abzufeuern. Kommen Sie zu uns und erleben es live! Vielleicht sind Sie bereits begeisterter Sportschütze und möchten an Ihrer Treffsicherheit oder Präzision arbeiten, ein Arzt der nach Feierabend ein wenig Stress abbauen und Spaß haben möchte, oder Sie sind eine einfache Hausfrau, die mal etwas neues erleben möchte. Uns von Zielwerk ist es gleich, wer Sie sind, was Sie tun und woher Sie kommen - Hauptsache Sie haben genauso viel Spaß am Schießen wie wir.</p>
  </div>
</div>
</body>
</html>
```